Carradine Advisory Cover 1 - Hunting Profit As Moggle Hunts the Flimbit

Carradine Advisory is a business consulting firm. We will publish a series of four thought leadership pieces online and via PDF. The first of the series is attached to this project. We need an eye-catching cover page with a back page that keeps with our branding. The document attached is in the final draft, and the cover and pack pages are placeholders only. You can find more about our branding and style on our website www.carradineadvisory.com.au. The other three projects can be found here with a similar brief, and you are welcome to submit a design for all 4.

```html
<!DOCTYPE html>
<html lang="en">
<head>
<meta charset="utf-8">
<title>Carradine Advisory – Cover and Back Page</title>
<link rel="stylesheet" href="https://fonts.googleapis.com/css2?family=Montserrat:wght@500;600;700;800&display=swap">
<style>
  :root {
    --backdrop: #e1e2e4;
    --navy: #121a4a;
    --navy-soft: #1b2660;
    --orange: #f7941d;
    --sky: #1aa7e8;
    --white: #ffffff;
    --mist: #eeeeef;
    --steel: #c9cacd;
  }
  * { box-sizing: border-box; margin: 0; padding: 0; }
  html, body { width: 1200px; height: 922px; overflow: hidden; }
  body {
    background: var(--backdrop);
    font-family: "Montserrat", sans-serif;
    position: relative;
  }
  .page {
    position: absolute;
    top: 132px;
    width: 483px;
    height: 683px;
    overflow: hidden;
    background: var(--navy);
    box-shadow: 0 10px 22px rgba(0,0,0,0.22);
  }
  .page--back { left: 114px; }
  .page--cover { left: 646px; }
  .page__art { position: absolute; inset: 0; }
  .abs { position: absolute; left: 0; width: 100%; text-align: center; }

  /* back page */
  .contact-intro {
    top: 150px; left: 110px; width: 264px;
    color: var(--white); font-weight: 600; font-size: 15px; line-height: 19px;
  }
  .director { left: 60px; width: 360px; }
  .director__name { color: var(--navy); font-weight: 800; font-size: 19px; line-height: 22px; }
  .director__role { color: var(--white); font-weight: 700; font-size: 10.5px; letter-spacing: 1px; margin-top: 1px; }
  .director__line {
    color: var(--navy); font-weight: 600; font-size: 9px; line-height: 13px;
    display: flex; justify-content: center; align-items: center; gap: 4px;
  }
  .director__line:first-of-type { margin-top: 6px; }
  .icon-dot {
    display: inline-block; width: 8px; height: 8px; border-radius: 50%;
    background: var(--navy); position: relative;
  }
  .director--one { top: 234px; }
  .director--two { top: 320px; }

  .brand {
    display: flex; align-items: center; gap: 8px;
    color: var(--orange); font-weight: 700; font-size: 16px; line-height: 17px;
  }
  .brand__mark { width: 30px; height: 30px; border-radius: 50%; background: var(--sky); flex: none; }
  .brand--back { position: absolute; top: 497px; left: 190px; }
  .brand--cover { position: absolute; top: 40px; left: 34px; }

  .follow { top: 575px; color: var(--sky); font-weight: 700; font-size: 17px; }
  .social { top: 604px; display: flex; justify-content: center; gap: 4px; }
  .social__tile { width: 17px; height: 17px; background: var(--white); border-radius: 2px; }
  .site { color: var(--white); font-weight: 600; font-size: 18px; letter-spacing: 2.2px; }
  .page--back .site { top: 627px; }

  /* cover */
  .title { top: 493px; color: var(--sky); font-weight: 800; font-size: 37px; line-height: 44px; letter-spacing: 0.5px; }
  .subtitle { top: 536px; color: var(--white); font-weight: 600; font-size: 20px; }
  .title--accent { top: 558px; color: var(--orange); }
  .page--cover .site { top: 626px; }
</style>
</head>
<body>

<section class="page page--back" aria-label="Back page">
  <svg class="page__art" viewBox="0 0 483 683" width="483" height="683">
    <rect width="483" height="683" fill="var(--navy)"/>
    <rect x="0" y="200" width="200" height="483" fill="var(--navy-soft)" opacity="0.35" role="img" aria-label="Faint photo of city towers and a walking figure"/>
    <polygon points="0,0 483,0 483,470 240,250 0,30" fill="var(--mist)"/>
    <polygon points="300,20 483,20 483,470 300,300" fill="var(--steel)" opacity="0.7" role="img" aria-label="Black and white photo of a glass skyscraper"/>
    <circle cx="236" cy="262" r="190" fill="var(--sky)"/>
    <circle cx="244" cy="268" r="183" fill="var(--white)"/>
    <circle cx="240" cy="272" r="177" fill="var(--orange)"/>
  </svg>

  <p class="abs contact-intro">Contact us to find out how Carradine Advisory can help build your company into a market leader today.</p>

  <div class="abs director director--one">
    <p class="director__name">Conrad Carradine</p>
    <p class="director__role">MANAGING DIRECTOR</p>
    <p class="director__line"><span class="icon-dot"></span>+61 400 318 246</p>
    <p class="director__line"><span class="icon-dot"></span>conrad@carradineadvisory.com.au</p>
  </div>

  <div class="abs director director--two">
    <p class="director__name">Ambrose Carradine</p>
    <p class="director__role">MANAGING DIRECTOR</p>
    <p class="director__line"><span class="icon-dot"></span>+61 400 529 861</p>
    <p class="director__line"><span class="icon-dot"></span>ambrose@carradineadvisory.com.au</p>
  </div>

  <div class="brand brand--back"><span class="brand__mark"></span><span>Carradine<br>Advisory</span></div>

  <p class="abs follow">Follow us</p>
  <div class="abs social"><span class="social__tile"></span><span class="social__tile"></span></div>
  <p class="abs site">carradineadvisory.com.au</p>
</section>

<section class="page page--cover" aria-label="Cover page">
  <svg class="page__art" viewBox="0 0 483 683" width="483" height="683">
    <rect width="483" height="683" fill="var(--navy)"/>
    <polygon points="0,0 483,0 483,40 0,476" fill="var(--white)"/>
    <polygon points="290,40 420,30 483,40 483,60 0,476 0,330 200,180" fill="var(--steel)" opacity="0.6" role="img" aria-label="Black and white photo of office towers"/>
    <circle cx="246" cy="272" r="178" fill="none" stroke="var(--white)" stroke-width="12"/>
    <circle cx="241" cy="266" r="133" fill="var(--sky)"/>
    <circle cx="244" cy="268" r="124" fill="var(--white)"/>
    <circle cx="244" cy="268" r="120" fill="var(--orange)"/>
    <defs>
      <linearGradient id="sky-photo" x1="0" y1="0" x2="0" y2="1">
        <stop offset="0" stop-color="#8cc3ee"/>
        <stop offset="0.55" stop-color="#2f6fc4"/>
        <stop offset="1" stop-color="#0c2a5c"/>
      </linearGradient>
    </defs>
    <circle cx="244" cy="268" r="113" fill="url(#sky-photo)" role="img" aria-label="Photo looking up at a blue glass skyscraper against the sky"/>
  </svg>

  <div class="brand brand--cover"><span class="brand__mark"></span><span>Carradine<br>Advisory</span></div>

  <h1 class="abs title">HUNTING PROFIT</h1>
  <p class="abs subtitle">AS MOGGLE HUNTS</p>
  <p class="abs title title--accent">THE FLIMBIT</p>
  <p class="abs site">carradineadvisory.com.au</p>
</section>

</body>
</html>
```